Startup Biz for Seniors needs your help!

Our business is a Startup that Employs Caregivers to do IN HOME Care of the Elderly. Our website is not yet running. But, a business similar to ours is Tallbrookcare.com

We are looking for a card that only has 4 Elements:
-Logo
- Website
- Tag Line
- Phone
We would like to see some eye catching backgrounds.
We would like to see some designs with and some without a Photo.
Would like the Photo to be of a Caregiver taking care of a Senior. The photo should show both of them smiling.

Target Market(s)

Age 35-55 who has Parents that are Elderly and need care

Industry/Entity Type

Home Health Care

Contact Information for Business Card

Want it to Pop Out to the viewer . Thinking maybe:
Side 1: LOGO with Website & Tag line
Side 2: Phone Number

Font styles to use
Other font styles liked:
• Same Font as our Logo

Colors

Designer to choose colors to be used in the design.

Requirements
Must have
• Logo, website, Tag Line, Phone number and Email: "info@velvetdays.example"
• Please use one of the photos that I have attached.
Nice to have
• Would like to see a Photo worked in that has a Care Taker taking care of an Elderly Person and they are both smiling.

```html
<!DOCTYPE html>
<html lang="en">
<head>
<meta charset="utf-8">
<title>Velvet Days – Business Card</title>
<link rel="stylesheet" href="https://fonts.googleapis.com/css2?family=Baloo+2:wght@700&family=Lobster+Two:ital,wght@1,700&display=swap">
<style>
  :root {
    --backdrop-top: #5a4f86;
    --backdrop-bottom: #4a3560;
    --card-pink: #d98cb4;
    --card-magenta: #b0457f;
    --card-plum: #5e2657;
    --card-deep: #4a1c48;
    --card-mist: #8a88a8;
    --frame: #ffffff;
    --ornament-a: rgba(205, 185, 235, 0.55);
    --ornament-b: rgba(170, 150, 215, 0.25);
    --ink: #ffffff;
    --art-light: rgba(255, 255, 255, 0.30);
    --art-soft: rgba(255, 255, 255, 0.18);
  }
  * { margin: 0; padding: 0; box-sizing: border-box; }
  html, body { width: 1200px; height: 1000px; overflow: hidden; }
  body {
    position: relative;
    background: linear-gradient(160deg, var(--backdrop-top), var(--backdrop-bottom));
    font-family: "Baloo 2", system-ui, sans-serif;
  }
  .card {
    position: absolute;
    left: 310px;
    width: 580px;
    height: 358px;
    overflow: hidden;
    background:
      radial-gradient(ellipse 180px 260px at 190px 40px, rgba(235, 170, 205, 0.75), transparent 70%),
      radial-gradient(ellipse 260px 200px at 560px 320px, rgba(140, 140, 175, 0.85), transparent 75%),
      radial-gradient(ellipse 260px 160px at 250px 350px, var(--card-deep), transparent 80%),
      linear-gradient(90deg, var(--card-magenta) 0%, var(--card-pink) 32%, var(--card-plum) 58%, #6a3a70 80%, var(--card-mist) 100%);
  }
  .card--front { top: 108px; }
  .card--back { top: 533px; }
  .card__frame {
    position: absolute;
    inset: 18px 20px 16px 20px;
    border: 1.5px solid var(--frame);
  }
  .card__ornament {
    position: absolute;
    top: 30px;
    bottom: 20px;
    width: 92px;
    border-radius: 40px;
    background: radial-gradient(ellipse at center, var(--ornament-a), var(--ornament-b) 60%, transparent 85%);
  }
  .card__ornament--left { left: -6px; }
  .card__ornament--right { right: -6px; }

  .brand {
    position: absolute;
    left: 130px;
    top: 140px;
    display: flex;
    align-items: center;
    gap: 12px;
  }
  .brand__dot {
    width: 64px; height: 64px;
    border-radius: 50%;
    background: var(--ink);
    flex: none;
  }
  .brand__name {
    color: var(--ink);
    font-size: 29px;
    line-height: 1;
    font-weight: 700;
  }
  .brand__tagline {
    margin-top: 6px;
    margin-left: 30px;
    color: var(--ink);
    font-family: "Lobster Two", "Georgia", cursive;
    font-style: italic;
    font-weight: 700;
    font-size: 16px;
    line-height: 1;
  }

  .phone-art {
    position: absolute;
    left: 185px;
    top: 87px;
    width: 210px;
    height: 185px;
    border-radius: 40px 40px 14px 14px;
    background: radial-gradient(ellipse at 50% 45%, var(--art-light), var(--art-soft) 65%, transparent 95%);
  }
  .phone__number {
    position: absolute;
    left: 185px;
    width: 210px;
    top: 168px;
    text-align: center;
    color: var(--ink);
    font-size: 32px;
    font-weight: 700;
    line-height: 33px;
    letter-spacing: 1px;
    text-shadow: 1px 2px 0 #3a1e3e;
  }
</style>
</head>
<body>
  <section class="card card--front" aria-label="Business card front">
    <div class="card__ornament card__ornament--left" role="img" aria-label="Lilac swirling leaf vine ornament"></div>
    <div class="card__ornament card__ornament--right" role="img" aria-label="Lilac swirling leaf vine ornament"></div>
    <div class="card__frame"></div>
    <div class="brand">
      <span class="brand__dot"></span>
      <div>
        <p class="brand__name">velvetdays.example</p>
        <p class="brand__tagline">Senior Care - Family Style</p>
      </div>
    </div>
  </section>

  <section class="card card--back" aria-label="Business card back">
    <div class="card__ornament card__ornament--left" role="img" aria-label="Lilac swirling leaf vine ornament"></div>
    <div class="card__ornament card__ornament--right" role="img" aria-label="Lilac swirling leaf vine ornament"></div>
    <div class="card__frame"></div>
    <div class="phone-art" role="img" aria-label="Large faint vintage telephone illustration behind the phone number"></div>
    <p class="phone__number">888<br>555<br>0142</p>
  </section>
</body>
</html>
```